Powder detergent

We need a design for packaging of powder detergent. Packaging is plastic 3 kg. Brand of product is VORU. Current sub-brand is Glintrax 4. We suggest to change sub-brand using 'Lumina white', 'Lumina clean', 'Lumina color', whatever but keeping unchanged words VORU and Lumina.
Herewith attached you may find pictures of current designs we have.
If you need more info please let me know.
Updates

Target Market(s)

women 25-65 years old, in Albanian market

Industry/Entity Type

Plastic

Requirements
Must have
• Brand VORU must be unchanged in color and font.
The word 'Lumina' must be as sub-brand, free to be changed in color and font.

```html
<!DOCTYPE html>
<html lang="en">
<head>
<meta charset="utf-8">
<title>VORU Lumina White – Powder Detergent Packaging</title>
<link rel="stylesheet" href="https://fonts.googleapis.com/css2?family=Oswald:wght@500;700&display=swap">
<style>
  :root {
    --page-bg: #ffffff;
    --sea-blue: #1e8fd6;
    --sea-glow: #6cc8f5;
    --orchid-green: #97c93d;
    --orchid-glow: #eef7b8;
    --baby-pink: #ec246a;
    --baby-glow: #f9a6c4;
    --brand-red: #c9301c;
    --white: #ffffff;
    --ring-light: #f4f4f4;
    --ring-shade: #b9b9b9;
  }

  * { box-sizing: border-box; margin: 0; padding: 0; }

  html, body {
    width: 1200px;
    height: 778px;
    overflow: hidden;
    background: var(--page-bg);
  }

  .range {
    position: relative;
    width: 1200px;
    height: 778px;
  }

  .pack {
    position: absolute;
    top: 8px;
    width: 371px;
    height: 760px;
    overflow: hidden;
    font-family: "Oswald", "Arial Narrow", sans-serif;
    color: var(--white);
  }

  .pack--sea    { left: 22px;  --base: var(--sea-blue);     --glow: var(--sea-glow); }
  .pack--orchid { left: 418px; --base: var(--orchid-green); --glow: var(--orchid-glow); }
  .pack--baby   { left: 812px; --base: var(--baby-pink);    --glow: var(--baby-glow); }

  .pack__background {
    position: absolute;
    inset: 0;
    background:
      radial-gradient(ellipse 200px 190px at 190px 300px, var(--glow) 0%, transparent 75%),
      var(--base);
  }

  .pack__rays {
    position: absolute;
    left: 0;
    top: 100px;
    width: 371px;
    height: 400px;
    opacity: 0.35;
  }

  .brand {
    position: absolute;
    left: 0;
    right: 0;
    top: 236px;
    text-align: center;
    font-weight: 700;
    font-size: 142px;
    line-height: 1;
    letter-spacing: 2px;
    color: var(--brand-red);
  }

  .sub-brand {
    position: absolute;
    right: 34px;
    top: 390px;
    font-weight: 500;
    font-size: 38px;
    line-height: 1;
    letter-spacing: 0.5px;
    transform: rotate(-5deg);
    transform-origin: right center;
    text-shadow: 0 2px 4px rgba(0, 0, 0, 0.25);
  }

  .badge {
    position: absolute;
    left: 62px;
    top: 464px;
    width: 244px;
    height: 244px;
    border-radius: 50%;
    background: radial-gradient(circle at 40% 30%, var(--white) 0%, var(--ring-light) 55%, var(--ring-shade) 100%);
    box-shadow: 0 14px 22px rgba(0, 0, 0, 0.28);
  }

  .badge__visual {
    position: absolute;
    inset: 12px;
    border-radius: 50%;
  }

  .badge__visual--sea    { background: radial-gradient(circle at 45% 35%, #2c7fc2 0%, #0f4f8f 55%, #0a2e5a 100%); }
  .badge__visual--orchid { background: radial-gradient(circle at 60% 45%, #d27ad8 0%, #9a4ab5 55%, #6d2b8c 100%); }
  .badge__visual--baby   { background: radial-gradient(circle at 50% 45%, #f6dccb 0%, #eed6c8 50%, #f3f1ef 100%); }

  .pack__footer {
    position: absolute;
    left: 8px;
    right: 10px;
    bottom: 10px;
    display: flex;
    justify-content: space-between;
    align-items: center;
    font-weight: 500;
    font-size: 15px;
    line-height: 1;
    letter-spacing: 0.2px;
  }

  .net-content {
    display: flex;
    align-items: center;
    gap: 3px;
  }

  .net-content svg { width: 18px; height: 14px; }
</style>
</head>
<body>
<main class="range">

  <!-- Sea variant -->
  <section class="pack pack--sea">
    <div class="pack__background"></div>
    <svg class="pack__rays" viewBox="0 0 371 400" aria-hidden="true">
      <g fill="#ffffff">
        <polygon points="185,200 150,0 220,0"/>
        <polygon points="185,200 0,40 0,110"/>
        <polygon points="185,200 371,40 371,110"/>
        <polygon points="185,200 60,0 100,0"/>
        <polygon points="185,200 270,0 310,0"/>
      </g>
    </svg>
    <div class="brand">VORU</div>
    <div class="sub-brand">LUMINA WHITE</div>
    <div class="badge">
      <div class="badge__visual badge__visual--sea" role="img" aria-label="Underwater photo of a sea turtle swimming over a coral reef"></div>
    </div>
    <footer class="pack__footer">
      <span class="variant">SPIRIT OF THE SEA</span>
      <span class="net-content">30
        <svg viewBox="0 0 18 14" aria-hidden="true"><rect x="1" y="3" width="11" height="10" fill="#fff"/><rect x="11" y="1" width="6" height="3" fill="#fff"/></svg>
        3KG</span>
    </footer>
  </section>

  <!-- Orchid variant -->
  <section class="pack pack--orchid">
    <div class="pack__background"></div>
    <svg class="pack__rays" viewBox="0 0 371 400" aria-hidden="true">
      <g fill="#ffffff">
        <polygon points="185,200 150,0 220,0"/>
        <polygon points="185,200 0,40 0,110"/>
        <polygon points="185,200 371,40 371,110"/>
        <polygon points="185,200 60,0 100,0"/>
        <polygon points="185,200 270,0 310,0"/>
      </g>
    </svg>
    <div class="brand">VORU</div>
    <div class="sub-brand">LUMINA WHITE</div>
    <div class="badge">
      <div class="badge__visual badge__visual--orchid" role="img" aria-label="Photo of pink orchid blossoms on a soft purple background"></div>
    </div>
    <footer class="pack__footer">
      <span class="variant">ORCHIDEA</span>
      <span class="net-content">30
        <svg viewBox="0 0 18 14" aria-hidden="true"><rect x="1" y="3" width="11" height="10" fill="#fff"/><rect x="11" y="1" width="6" height="3" fill="#fff"/></svg>
        3KG</span>
    </footer>
  </section>

  <!-- Baby care variant -->
  <section class="pack pack--baby">
    <div class="pack__background"></div>
    <svg class="pack__rays" viewBox="0 0 371 400" aria-hidden="true">
      <g fill="#ffffff">
        <polygon points="185,200 150,0 220,0"/>
        <polygon points="185,200 0,40 0,110"/>
        <polygon points="185,200 371,40 371,110"/>
        <polygon points="185,200 60,0 100,0"/>
        <polygon points="185,200 270,0 310,0"/>
      </g>
    </svg>
    <div class="brand">VORU</div>
    <div class="sub-brand">LUMINA WHITE</div>
    <div class="badge">
      <div class="badge__visual badge__visual--baby" role="img" aria-label="Photo of a smiling baby lying on a white towel"></div>
    </div>
    <footer class="pack__footer">
      <span class="variant">BABY CARE</span>
      <span class="net-content">30
        <svg viewBox="0 0 18 14" aria-hidden="true"><rect x="1" y="3" width="11" height="10" fill="#fff"/><rect x="11" y="1" width="6" height="3" fill="#fff"/></svg>
        3KG</span>
    </footer>
  </section>

</main>
</body>
</html>
```